Elevating our current Business Card Design

We want to elevate our current business card with a new design to look like a marlow 800 company. We are a premium lubricant distributor (oil and grease).
We need 2 versions, version 1 is as per the uploaded a copy of our current business card with the English version.
For our Chinese version we need to use the front to be English in English and have the back of the card designed exactly like the front for all info to be in Chinese.
The design template needs to be such that we can amend the template with adding different information for each person's card.
The background colour of the card can be changed- we just need to clearly see all information on the card and logos.
The TRV and Verdant Mark logos cannot have any colour or display changes- only use the logos attached.
All logos need to be included and all information from the attached current card

```html
<!DOCTYPE html>
<html lang="en">
<head>
<meta charset="utf-8">
<title>Meridian Business Card</title>
<link rel="stylesheet" href="https://fonts.googleapis.com/css2?family=Open+Sans:wght@400;600;700&family=Ubuntu:wght@500&display=swap">
<style>
  :root {
    --stage: #232323;
    --card-dark: #1e1e1e;
    --red: #e32b24;
    --red-deep: #c0201b;
    --white: #ffffff;
    --gold: #d29e2a;
    --gold-light: #e8bd3c;
    --badge-grey: #8a8a8a;
    --badge-orange: #f07a22;
    --cert-green: #1f5a36;
  }
  * { margin: 0; padding: 0; box-sizing: border-box; }
  html, body { width: 1200px; height: 780px; overflow: hidden; background: var(--stage); }
  .canvas { position: relative; width: 1200px; height: 780px; }
  .card {
    position: absolute; top: 227px; width: 570px; height: 326px; overflow: hidden;
    box-shadow: 0 10px 28px rgba(0,0,0,.55);
  }
  /* back side */
  .card-back { left: 20px; }
  .gold-pattern {
    position: absolute; inset: 0;
    background: radial-gradient(circle at 40% 40%, var(--gold-light), var(--gold) 70%);
  }
  .brand-mark {
    position: absolute; display: flex; align-items: center; gap: 14px;
    font-family: "Open Sans", sans-serif; font-weight: 700; color: var(--red);
  }
  .card-back .brand-mark { left: 50%; top: 50%; transform: translate(-50%, -50%); font-size: 64px; letter-spacing: 2px; }
  .brand-dot { border-radius: 50%; flex: none; }
  .card-back .brand-dot { width: 56px; height: 56px; background: var(--white); }

  /* front side */
  .card-front { right: 20px; background: var(--card-dark); }
  .card-front .brand-mark { right: 30px; top: 30px; font-size: 42px; letter-spacing: 1px; }
  .card-front .brand-dot { width: 36px; height: 36px; background: var(--gold-light); }

  .timeline { position: absolute; left: 0; top: 0; width: 70px; height: 326px; }
  .person-name {
    position: absolute; left: 74px; top: 34px;
    font-family: "Ubuntu", sans-serif; font-weight: 500; font-size: 30px; color: var(--red);
  }
  .person-title {
    position: absolute; left: 76px; top: 72px;
    font-family: "Open Sans", sans-serif; font-weight: 600; font-size: 14px; color: var(--white);
  }
  .contact-list {
    position: absolute; left: 76px; top: 118px; list-style: none;
    font-family: "Open Sans", sans-serif; font-size: 14.5px; color: var(--white); line-height: 23px;
  }
  .address {
    position: absolute; left: 76px; top: 250px;
    font-family: "Open Sans", sans-serif; font-size: 14.5px; color: var(--white); line-height: 21px;
  }
  .badge-row { position: absolute; right: 28px; top: 150px; display: flex; gap: 16px; align-items: flex-end; }
  .badge-cert { width: 60px; height: 38px; border-radius: 20px 20px 6px 6px; background: var(--cert-green); }
  .badge-iso { width: 46px; height: 46px; border-radius: 50%; background: var(--badge-orange); border: 4px solid var(--badge-grey); }
  .partner-strip { position: absolute; right: 28px; top: 222px; display: flex; height: 56px; }
  .partner-box {
    display: flex; align-items: center; padding: 0 14px;
    border: 2px solid var(--red); border-right: none;
    font-family: "Open Sans", sans-serif; font-weight: 700; font-size: 11px; color: var(--red); line-height: 13px;
  }
  .supplier-band {
    display: flex; align-items: center; padding: 0 20px; background: var(--red);
    font-family: "Open Sans", sans-serif; font-weight: 700; font-size: 24px; color: var(--white); letter-spacing: 1px;
  }
</style>
</head>
<body>
<main class="canvas">
  <section class="card card-back" aria-label="Card back">
    <div class="gold-pattern" role="img" aria-label="Embossed gold foil repeating pattern"></div>
    <div class="brand-mark"><span class="brand-dot"></span>MERIDIAN</div>
  </section>

  <section class="card card-front" aria-label="Card front">
    <svg class="timeline" viewBox="0 0 70 326" aria-hidden="true">
      <line x1="22" y1="20" x2="60" y2="320" stroke="var(--red)" stroke-width="1.5"/>
      <g fill="var(--red-deep)">
        <rect x="14" y="70" width="28" height="28" transform="rotate(45 28 84)"/>
        <rect x="47" y="122" width="14" height="14" transform="rotate(45 54 129)"/>
        <rect x="47" y="145" width="14" height="14" transform="rotate(45 54 152)"/>
        <rect x="47" y="168" width="14" height="14" transform="rotate(45 54 175)"/>
        <rect x="47" y="191" width="14" height="14" transform="rotate(45 54 198)"/>
        <rect x="47" y="214" width="14" height="14" transform="rotate(45 54 221)"/>
        <rect x="47" y="254" width="14" height="14" transform="rotate(45 54 261)"/>
      </g>
      <g fill="var(--white)">
        <circle cx="28" cy="79" r="4"/>
        <path d="M20 92 q8 -10 16 0 z"/>
        <path d="M51 126 h2 l1 3 -1 1 q1 2 2 2 l1 -1 3 1 v2 q-6 0 -8 -8 z"/>
        <rect x="52" y="148" width="4" height="8" rx="1"/>
        <rect x="51" y="172" width="6" height="5"/>
        <circle cx="54" cy="198" r="3.5"/>
        <rect x="50.5" y="219" width="7" height="5"/>
        <path d="M54 257 a3 3 0 0 1 3 3 q0 2 -3 5 q-3 -3 -3 -5 a3 3 0 0 1 3 -3 z"/>
      </g>
    </svg>

    <h1 class="person-name">Clara Benning</h1>
    <p class="person-title">Administration Executive</p>

    <ul class="contact-list">
      <li>1300 427 615</li>
      <li>+61 412 880 374</li>
      <li>+61 8 9204 5530</li>
      <li>www.meridianoil.com</li>
      <li>clara.benning@meridianoil.com</li>
    </ul>
    <p class="address">48 Depot Parade<br>Ashby Vale, WA 6190</p>

    <div class="brand-mark"><span class="brand-dot"></span>MERIDIAN</div>

    <div class="badge-row">
      <span class="badge-cert" role="img" aria-label="Verdant Mark certification"></span>
      <span class="badge-iso" role="img" aria-label="TRV ISO certification"></span>
      <span class="badge-iso" role="img" aria-label="TRV ISO certification"></span>
      <span class="badge-iso" role="img" aria-label="TRV ISO certification"></span>
    </div>

    <div class="partner-strip">
      <div class="partner-box">MERIDIAN OIL<br>DISTRIBUTORS</div>
      <div class="supplier-band">HALVERN</div>
    </div>
  </section>
</main>
</body>
</html>
```